Piano genealogy graphs template, for a large poster printing

Hello and thank you for your interest in my project.
I need a poster template, so I can create structures similar to the one I have uploaded. I want to completely replace or improve my poor previous design which is attached.
I need to be able to input names and dates into boxes of various colors, arrows pointing between boxes. I would also like to be able to label each graph (not each box).
I am looking at something that would be legible when printed, in a one consistent professional layout of 2A0 (around 1189x1682 mm) poster (I know it is large). The design template required here can include just few sample text boxes with sample flags on a suitable background, for me to multiply later and spread across the whole poster.
The positioning of the boxes is not important.
Please let me know if more clarification is required.
Thank you for your help.

Feel free to follow what I have attached in the file, or change the design completely.

UPDATE 4/12: I have uploaded two more graphs as an example. At this stage of the contest, I would like to have one of those graphs done, and I am planning to offer a 'freelance job' to one or two designers, who will be willing to do the whole 10 graphs on one poster.
Updates

Reason: Dear Designers, Since the project is rather complex and large-scale, I have decided to give everyone more time to work on their designs. I will consider extending it further if any of you require additional time. Best wishes, bronisław

Dear Designers, I would like to inform you that the contest for my poster is now closed and that I have assigned the prizes. I would like to thank all of you for submiting your high-quality designs, and for your participation. It was a great pleasure working with all of you. Due to the large size of the project itself (large number of graphs to be fitted on a single poster), I had to focus on providing feedback to only those designers who provided projects closest to what I was expecting at the early stages of the contest. I wish you all the best for the future, Kind regards, Bronisław

Target Market(s)

Pianists, historians

Industry/Entity Type

Printing

Requirements
Must have
• Consistent design, but allow to clearly delineate various genealogy trees.

```html
<!DOCTYPE html>
<html lang="en">
<head>
<meta charset="utf-8">
<title>Hungarian influences — Piano Genealogy</title>
<link rel="stylesheet" href="https://fonts.googleapis.com/css2?family=Lato:ital,wght@0,300;0,400;1,400&display=swap">
<style>
  :root {
    --paper: #f6f5e6;
    --paper-warm: #f3f1cf;
    --ink: #1c1c1c;
    --panel-dark: #c6c6bd;
    --panel-mid: #d9d9cf;
    --students-bg: #f4f2d6;
    --accent-green: #7fbf6e;
    --hu-red: #d92f2a;
    --hu-green: #3f9a3a;
    --us-red: #c8283a;
    --us-blue: #2c3a7a;
    --il-blue: #2851b5;
  }
  html, body {
    margin: 0; padding: 0;
    width: 1111px; height: 1200px;
    overflow: hidden;
    background: #fff;
  }
  .poster {
    position: relative;
    width: 1111px; height: 1200px;
    overflow: hidden;
    font-family: 'Lato', Arial, sans-serif;
    color: var(--ink);
  }
  .poster-bg {
    position: absolute; left: 24px; top: 24px; width: 1087px; height: 1176px;
    background: linear-gradient(160deg, #eef1dd 0%, var(--paper) 45%, var(--paper-warm) 100%);
  }
  .corner-accent { position: absolute; left: 0; top: 0; }
  .branch-label {
    position: absolute; left: 36px; top: 1140px;
    transform: rotate(-90deg); transform-origin: 0 0;
    font-weight: 300; font-size: 98px; line-height: 1; white-space: nowrap;
    letter-spacing: 1px;
  }
  .graph-title {
    position: absolute; left: 198px; top: 16px; margin: 0;
    font-weight: 300; font-size: 92px; line-height: 1.1;
  }
  .branch-panel {
    position: absolute; left: 346px; width: 750px;
    background: linear-gradient(90deg, var(--panel-dark) 0%, var(--panel-mid) 55%, rgba(230,230,222,0.3) 100%);
    box-shadow: 0 3px 6px rgba(0,0,0,0.18), 0 0 14px rgba(200,200,190,0.8);
    border-radius: 2px;
  }
  .students-box {
    position: absolute; left: 422px; width: 378px;
    background: linear-gradient(90deg, #e8e6c8 0%, var(--students-bg) 30%, #f6f5e3 100%);
    box-shadow: 0 0 10px rgba(160,160,150,0.55);
  }
  .entry {
    position: absolute; display: flex; align-items: center; gap: 4px;
    font-size: 18px; line-height: 26px; white-space: nowrap;
  }
  .entry .name { margin-right: 2px; }
  .entry--root { font-size: 18px; text-decoration: underline; text-underline-offset: 4px; }
  .entry--heading { font-style: italic; }
  .flag { width: 40px; height: 26px; display: block; }
</style>
</head>
<body>
<svg width="0" height="0" style="position:absolute" aria-hidden="true">
  <defs>
    <symbol id="flag-hu" viewBox="0 0 40 26">
      <rect width="40" height="8.7" fill="var(--hu-red)"/>
      <rect y="8.7" width="40" height="8.6" fill="#fff"/>
      <rect y="17.3" width="40" height="8.7" fill="var(--hu-green)"/>
    </symbol>
    <symbol id="flag-il" viewBox="0 0 40 26">
      <rect width="40" height="26" fill="#fff"/>
      <rect y="2.5" width="40" height="3.5" fill="var(--il-blue)"/>
      <rect y="20" width="40" height="3.5" fill="var(--il-blue)"/>
      <path d="M20 8.2 L24 15 L16 15 Z M20 17.8 L16 11 L24 11 Z" fill="none" stroke="var(--il-blue)" stroke-width="1"/>
    </symbol>
    <symbol id="flag-us" viewBox="0 0 40 26">
      <rect width="40" height="26" fill="#fff"/>
      <g fill="var(--us-red)">
        <rect y="0" width="40" height="2"/><rect y="4" width="40" height="2"/>
        <rect y="8" width="40" height="2"/><rect y="12" width="40" height="2"/>
        <rect y="16" width="40" height="2"/><rect y="20" width="40" height="2"/>
        <rect y="24" width="40" height="2"/>
      </g>
      <rect width="17" height="14" fill="var(--us-blue)"/>
    </symbol>
    <symbol id="flag-uk" viewBox="0 0 40 26">
      <rect width="40" height="26" fill="#243b8a"/>
      <path d="M0 0 L40 26 M40 0 L0 26" stroke="#fff" stroke-width="5"/>
      <path d="M0 0 L40 26 M40 0 L0 26" stroke="var(--us-red)" stroke-width="1.6"/>
      <path d="M20 0 V26 M0 13 H40" stroke="#fff" stroke-width="8"/>
      <path d="M20 0 V26 M0 13 H40" stroke="var(--us-red)" stroke-width="4.5"/>
    </symbol>
    <symbol id="flag-kr" viewBox="0 0 40 26">
      <rect width="40" height="26" fill="#fff"/>
      <circle cx="20" cy="13" r="6" fill="#2a4aa0"/>
      <path d="M14 13 A6 6 0 0 1 26 13 Z" fill="var(--us-red)"/>
      <g stroke="#111" stroke-width="1.4">
        <path d="M6 5 L10 8 M34 5 L30 8 M6 21 L10 18 M34 21 L30 18"/>
      </g>
    </symbol>
    <symbol id="flag-rs" viewBox="0 0 40 26">
      <rect width="40" height="8.7" fill="#c6363c"/>
      <rect y="8.7" width="40" height="8.6" fill="#0c4076"/>
      <rect y="17.3" width="40" height="8.7" fill="#fff"/>
    </symbol>
    <linearGradient id="green-wedge" x1="0" y1="0" x2="1" y2="0">
      <stop offset="0" stop-color="var(--accent-green)" stop-opacity="0"/>
      <stop offset="1" stop-color="var(--accent-green)" stop-opacity="0.9"/>
    </linearGradient>
    <linearGradient id="green-edge" x1="0" y1="0" x2="0" y2="1">
      <stop offset="0" stop-color="var(--accent-green)" stop-opacity="0.1"/>
      <stop offset="1" stop-color="var(--accent-green)" stop-opacity="0.9"/>
    </linearGradient>
  </defs>
</svg>

<main class="poster">
  <div class="poster-bg"></div>
  <svg class="corner-accent" width="1111" height="1200" aria-hidden="true">
    <polygon points="1104,24 1111,24 1111,1200 1090,1200" fill="url(#green-edge)"/>
    <polygon points="1100,1130 1111,1130 1111,1200 900,1200" fill="url(#green-wedge)"/>
  </svg>

  <div class="branch-label">American Tree, Branch IV</div>
  <h1 class="graph-title">Hungarian influences</h1>

  <!-- Panels -->
  <div class="branch-panel" style="top:276px;height:168px"></div>
  <div class="students-box" style="top:340px;height:96px"></div>

  <div class="branch-panel" style="top:496px;height:336px"></div>
  <div class="students-box" style="top:564px;height:92px"></div>
  <div class="students-box" style="top:696px;height:130px"></div>

  <div class="branch-panel" style="top:888px;height:308px"></div>
  <div class="students-box" style="top:924px;height:96px"></div>
  <div class="students-box" style="top:1056px;height:136px"></div>

  <!-- Root -->
  <div class="entry entry--root" style="left:244px;top:140px"><span class="name">FERENC HALMY (1811-1886)</span><svg class="flag"><use href="#flag-hu"/></svg></div>
  <div class="entry" style="left:280px;top:210px"><span class="name">Imre Dorosz (1862-1940)</span><svg class="flag"><use href="#flag-hu"/></svg></div>

  <!-- Branch 1 -->
  <div class="entry" style="left:356px;top:240px"><span class="name">Gábor Várkonyi (1881-1945)</span><svg class="flag"><use href="#flag-hu"/></svg></div>
  <div class="entry" style="left:430px;top:271px"><span class="name">Lajos Fehér (1912-2005)</span><svg class="flag"><use href="#flag-hu"/></svg></div>
  <div class="entry" style="left:430px;top:301px"><span class="name">Judit Ormos-Lenk (1901-1998)</span><svg class="flag"><use href="#flag-hu"/></svg><svg class="flag"><use href="#flag-il"/></svg></div>
  <div class="entry entry--heading" style="left:467px;top:336px"><span class="name">Students:</span></div>
  <div class="entry" style="left:467px;top:369px"><span class="name">Miriam Adelstein (1947)</span><svg class="flag"><use href="#flag-il"/></svg><svg class="flag"><use href="#flag-us"/></svg></div>
  <div class="entry" style="left:467px;top:404px"><span class="name">Eitan Baram (1940)</span><svg class="flag"><use href="#flag-rs"/></svg><svg class="flag"><use href="#flag-us"/></svg></div>

  <!-- Branch 2 -->
  <div class="entry" style="left:356px;top:464px"><span class="name">Dénes Karády (1882-1967)</span><svg class="flag"><use href="#flag-hu"/></svg></div>
  <div class="entry" style="left:430px;top:495px"><span class="name">Lajos Fehér (1912-2005)</span><svg class="flag"><use href="#flag-hu"/></svg></div>
  <div class="entry" style="left:430px;top:525px"><span class="name">Tibor Halász (1922-1999)</span><svg class="flag"><use href="#flag-hu"/></svg><svg class="flag"><use href="#flag-us"/></svg></div>
  <div class="entry entry--heading" style="left:467px;top:560px"><span class="name">Students:</span></div>
  <div class="entry" style="left:467px;top:593px"><span class="name">Nils Aldgren (1947)</span><svg class="flag"><use href="#flag-us"/></svg></div>
  <div class="entry" style="left:467px;top:628px"><span class="name">Min Jae Seo (1940)</span><svg class="flag"><use href="#flag-kr"/></svg><svg class="flag"><use href="#flag-us"/></svg></div>
  <div class="entry" style="left:430px;top:658px"><span class="name">Erzsébet Vass (1893-1973)</span><svg class="flag"><use href="#flag-hu"/></svg><svg class="flag"><use href="#flag-uk"/></svg></div>
  <div class="entry entry--heading" style="left:467px;top:692px"><span class="name">Students:</span></div>
  <div class="entry" style="left:467px;top:727px"><span class="name">Paul-Henri Castel</span><svg class="flag"><use href="#flag-us"/></svg></div>
  <div class="entry" style="left:467px;top:760px"><span class="name">Laura Whitcombe (1946)</span><svg class="flag"><use href="#flag-us"/></svg></div>
  <div class="entry" style="left:467px;top:795px"><span class="name">Daniel Rosenthal (1946)</span><svg class="flag"><use href="#flag-il"/></svg><svg class="flag"><use href="#flag-us"/></svg></div>

  <!-- Branch 3 -->
  <div class="entry" style="left:356px;top:856px"><span class="name">Pál Szendrey (1885-1960)</span><svg class="flag"><use href="#flag-hu"/></svg></div>
  <div class="entry" style="left:430px;top:886px"><span class="name">Tibor Halász (1922-1999)</span><svg class="flag"><use href="#flag-hu"/></svg><svg class="flag"><use href="#flag-us"/></svg></div>
  <div class="entry entry--heading" style="left:467px;top:920px"><span class="name">Students:</span></div>
  <div class="entry" style="left:467px;top:955px"><span class="name">Nils Aldgren (1947)</span><svg class="flag"><use href="#flag-us"/></svg></div>
  <div class="entry" style="left:467px;top:988px"><span class="name">Min Jae Seo (1940)</span><svg class="flag"><use href="#flag-kr"/></svg><svg class="flag"><use href="#flag-us"/></svg></div>
  <div class="entry" style="left:430px;top:1019px"><span class="name">Erzsébet Vass (1893-1973)</span><svg class="flag"><use href="#flag-hu"/></svg><svg class="flag"><use href="#flag-uk"/></svg></div>
  <div class="entry entry--heading" style="left:467px;top:1053px"><span class="name">Students:</span></div>
  <div class="entry" style="left:467px;top:1088px"><span class="name">Paul-Henri Castel</span><svg class="flag"><use href="#flag-us"/></svg></div>
  <div class="entry" style="left:467px;top:1121px"><span class="name">Laura Whitcombe (1946)</span><svg class="flag"><use href="#flag-us"/></svg></div>
  <div class="entry" style="left:467px;top:1156px"><span class="name">Daniel Rosenthal (1946)</span><svg class="flag"><use href="#flag-il"/></svg><svg class="flag"><use href="#flag-us"/></svg></div>
</main>
</body>
</html>
```